Book Cover Design (poetry, prose, and original quotes Book) - Title: lantern & moss

FIRSTLY - my name is MARGOT HALVERSEN (pls use this)

Looking for a soft cover design (6" X 9") as well as an e-book cover design. I have ISBN bar code already. This soft cover will need spine design and area for back cover blurb. Number of pages is approx 210. The page count might change, but only by a few pages if anything.
The book is a collection of poems, prose, and quotes with chapter titles such as: pain, growth, hope, trust, love, and...so it is. It's meant to be inspiring and also a go to book people will reach for when searching for truth.

Tavi Brennan and Lark Odessa are similar in nature to content.

I have attached an PIXMEADOW image that I am thinking of.
Lower case in title and in my name (author)
San Serif font.

I like the idea of the book title to be along the lateral line (where water meets the sky).

I am open to book cover ideas like the poets noted above, but that style seems to be saturating the genre.

Target Market(s)

Will be selling on BQL (Verdano). Audience are people who are on a journey of self-discovery, personal empowerment, and spirituality.

Industry/Entity Type

Spiritual / Personal Growth / Poetry

Font styles to use
Sans Serif
Other font styles liked:
• Simplifica, alcubierre, stellar, gantic, kiona

Requirements
Must have
• Front, Spine, and Back cover / lower case in title and author's name
Nice to have
• I do like the look of Tavi Brennan and Lark Odessa's books, but I feel that style might be over done now, but I am open to a modern simple style like their books (see examples below). I would like my book to convey the feeling of resonance (vibration) and reflection (thoughts, ideas as a result of meditation)
Should not have
• I prefer simple designs, not a lot of clutter, or heavy typefaces. Definately do not want anything like birds or butterflies.

```html
<!DOCTYPE html>
<html lang="en">
<head>
<meta charset="utf-8">
<title>lantern &amp; moss — cover spread</title>
<link rel="stylesheet" href="https://fonts.googleapis.com/css2?family=Montserrat:wght@300;400;500;800&display=swap">
<style>
  :root {
    --page: #ffffff;
    --back-top: #1c5b75;
    --back-mid: #185069;
    --back-low: #123e51;
    --sky-pale: #d8e1e6;
    --sky-blue: #c3d9e3;
    --ridge: #47657a;
    --forest: #141f26;
    --lake: #3f647a;
    --lake-light: #b8d1dc;
    --ink-light: #ffffff;
    --ink-soft: #e4eef3;
    --title-blue: #3d6a80;
    --ink-dark: #263640;
    --barcode-box: #ffffff;
  }
  * { margin: 0; padding: 0; box-sizing: border-box; }
  html, body {
    width: 1200px; height: 1200px; overflow: hidden;
    background: var(--page);
  }
  .spread {
    position: absolute; left: 30px; top: 190px;
    width: 1140px; height: 820px;
    display: grid; grid-template-columns: 547px 59px 534px;
    font-family: "Montserrat", sans-serif;
  }
  .panel { position: relative; overflow: hidden; }
  .photo-fill { position: absolute; inset: 0; }
  .back .photo-fill {
    background: linear-gradient(180deg, var(--back-top) 0%, var(--back-mid) 48%, #154a60 62%, var(--back-low) 82%, #175068 100%);
  }
  .spine .photo-fill, .front .photo-fill {
    background: linear-gradient(180deg, var(--sky-pale) 0%, var(--sky-blue) 30%, #d6e0e5 44%, #a9bfcb 50%, var(--ridge) 56%, #22343f 64%, var(--forest) 73%, #1d2e38 78%, var(--lake) 87%, var(--lake-light) 100%);
  }
  .spine .photo-fill { filter: brightness(0.96); }

  .title-block {
    position: absolute; left: 0; right: 0; top: 154px;
    text-align: center;
  }
  .title-line-one {
    font-weight: 300; font-size: 32px; letter-spacing: 0.62em;
    padding-left: 0.62em; line-height: 40px;
  }
  .title-line-two {
    font-weight: 800; font-size: 38px; line-height: 44px; letter-spacing: -0.01em;
  }
  .title-reflection {
    font-weight: 800; font-size: 38px; line-height: 44px; letter-spacing: -0.01em;
    height: 30px; margin-top: -12px;
    transform: scaleY(-0.62); transform-origin: 50% 60%;
    opacity: 0.45;
    -webkit-mask-image: linear-gradient(0deg, #000 20%, transparent 95%);
    mask-image: linear-gradient(0deg, #000 20%, transparent 95%);
  }
  .back .title-line-one, .back .title-line-two { color: var(--ink-light); }
  .back .title-reflection { color: var(--ink-soft); }
  .front .title-line-one { color: var(--title-blue); }
  .front .title-line-two { color: var(--ink-dark); }
  .front .title-reflection { color: #6c8796; }

  .blurb {
    position: absolute; left: 82px; width: 376px; top: 297px;
    color: var(--ink-soft); font-size: 13.6px; line-height: 23.9px;
    text-align: justify; text-align-last: center;
  }
  .barcode-space {
    position: absolute; left: 303px; top: 681px;
    width: 153px; height: 93px; background: var(--barcode-box);
  }

  .spine-text {
    position: absolute; left: 50%;
    writing-mode: vertical-rl; transform: translateX(-50%);
    font-size: 14px; letter-spacing: 0.16em; white-space: nowrap;
  }
  .spine-author { top: 91px; color: var(--ink-dark); font-weight: 400; }
  .spine-title { top: 493px; color: var(--ink-light); font-weight: 400; }
  .spine-title strong { font-weight: 800; }

  .front-author {
    position: absolute; left: 0; right: 0; top: 756px;
    text-align: center; color: var(--ink-dark);
    font-weight: 500; font-size: 21px; letter-spacing: 0.14em;
  }
</style>
</head>
<body>
  <main class="spread">
    <section class="panel back">
      <div class="photo-fill" role="img" aria-label="Blue-tinted mountain lake with its reflection in still water"></div>
      <div class="title-block">
        <p class="title-line-one">lantern</p>
        <p class="title-line-two">&amp; moss</p>
        <p class="title-reflection" aria-hidden="true">&amp; moss</p>
      </div>
      <p class="blurb">Lorem Ipsum is simply dummy text of the printing and typesetting industry. Lorem Ipsum has been the industry's standard dummy text ever since the 1500s, when an unknown printer took a galley of type and scrambled it to make a type specimen book. It has survived not only five centuries, but also the leap into electronic typesetting, remaining essentially unchanged. It was popularised in the 1960s with the release of Pressmark sheets containing Lorem Ipsum passages, and more recently with desktop publishing software like Folio Layout including versions of Lorem Ipsum.</p>
      <div class="barcode-space" aria-label="Barcode area"></div>
    </section>

    <section class="panel spine">
      <div class="photo-fill" role="img" aria-label="Continuation of the misty mountain and lake scene"></div>
      <p class="spine-text spine-author">margot halversen</p>
      <p class="spine-text spine-title">lantern <strong>&amp; moss</strong></p>
    </section>

    <section class="panel front">
      <div class="photo-fill" role="img" aria-label="Misty mountains over a still lake with a small boat and its reflection"></div>
      <div class="title-block">
        <p class="title-line-one">lantern</p>
        <p class="title-line-two">&amp; moss</p>
        <p class="title-reflection" aria-hidden="true">&amp; moss</p>
      </div>
      <p class="front-author">margot halversen</p>
    </section>
  </main>
</body>
</html>
```